A Maverick Business Card for a Maverick Company!

We're a maverick, 'rule breaker' market research company that needs a maverick business card design to suit who we are!

All logos, colours and text are detailed in the attached briefing document.

Note Please ignore the 'Look & Feel' wizard results and refer ONLY to the attached brief.

```html
<!DOCTYPE html>
<html lang="en">
<head>
<meta charset="utf-8">
<title>Business Card – Market Research</title>
<link rel="stylesheet" href="https://fonts.googleapis.com/css2?family=Saira:ital,wght@0,400;1,700&display=swap">
<style>
  :root {
    --card-red: #ff0000;
    --card-border: #000000;
    --ink-light: #ffffff;
  }
  html, body {
    margin: 0;
    padding: 0;
    width: 1200px;
    height: 717px;
    overflow: hidden;
    background: var(--card-border);
  }
  .card {
    position: relative;
    box-sizing: border-box;
    width: 1200px;
    height: 717px;
    background: var(--card-red);
    border: 4px solid var(--card-border);
    color: var(--ink-light);
    font-family: "Saira", "Arial Narrow", sans-serif;
  }
  .benefits {
    position: absolute;
    left: 297px;
    top: 261px;
    margin: 0;
    padding: 0;
    list-style: none;
    font-size: 21px;
    line-height: 28.5px;
    font-weight: 400;
    letter-spacing: 0.1px;
  }
  .tagline {
    position: absolute;
    left: 202px;
    top: 372px;
    margin: 0;
    font-size: 29.5px;
    line-height: 36px;
    font-weight: 700;
    font-style: italic;
    letter-spacing: 0.1px;
  }
  .contact {
    position: absolute;
    left: 735px;
    top: 613px;
    display: flex;
    font-size: 20px;
    line-height: 27px;
    font-style: normal;
  }
  .contact-label {
    width: 94px;
  }
</style>
</head>
<body>
  <main class="card">
    <ul class="benefits">
      <li>Professional market research-tailored, inexpensive &amp; fast</li>
      <li>Take a data -centric approach to your decision making</li>
      <li>Submit an online research brief &amp; we will do the rest</li>
    </ul>
    <h1 class="tagline">Professional research without the big agency price tag</h1>
    <address class="contact">
      <span class="contact-label">Contact:</span>
      <span class="contact-address">
        Harbourline Executive Suites,<br>
        48 Kestrel Terrace,<br>
        Riverton Vic 3999
      </span>
    </address>
  </main>
</body>
</html>
```